Velmora Junior Reading & Counting Drive

Development of the (VJRCD) website. The Velmora Junior Reading and Counting Drive (VJRCD) is a Velmora Bureau of Schooling Project running in approximately 810 participating Gauteng Primary Schools. The project goals are to improve Language and Mathematics scores in participating schools.
The colors should be the same colors as Velmora Schooling bureau colors ( see logos)

Try bring in human element - this project is about improving literacy and numeracy levels of marginalized primary school children.

Target Market(s)

Education sector and general public

Industry/Entity Type

School

Requirements
Must have
• The primary navigation of the site must always be displayed on each page.
? Each section must have a main page where visitors can navigate to the sub items under the relevant section.
? The overall design concept for the website must be optimised in terms of brand identity, accessibility, usability and content distribution. Colours and images must be chosen according to VJRCD’s corporate identity requirements.
? The VJRCD’s logo should be present on the homepage and visible at all times during a person’s visit.

```html
<!DOCTYPE html>
<html lang="en">
<head>
<meta charset="utf-8">
<title>Velmora Junior Reading &amp; Counting Drive</title>
<link rel="stylesheet" href="https://fonts.googleapis.com/css2?family=Open+Sans:wght@400;600;700&display=swap">
<style>
:root{
  --navy:#2b3e84;
  --navy-deep:#22336e;
  --navy-foot:#1b2958;
  --orange:#f5a313;
  --orange-dark:#e08e00;
  --white:#ffffff;
  --ink:#1d1d1d;
  --body-text:#555a63;
  --card-news:#f3efe7;
  --card-projects:#efefef;
  --card-district:#eaedf8;
}
*{margin:0;padding:0;box-sizing:border-box}
html,body{width:1143px;height:1200px;overflow:hidden;background:var(--navy)}
body{font-family:"Open Sans",Arial,sans-serif}
.page{position:relative;width:1000px;height:1050px;transform:scale(1.143);transform-origin:0 0;background:var(--navy)}
.header-wave{position:absolute;left:0;top:0;z-index:2}
.main-nav{position:absolute;left:78px;top:4px;width:448px;height:27px;background:var(--navy);border-radius:14px;display:flex;gap:21px;padding-left:17px;align-items:center;white-space:nowrap;z-index:3}
.main-nav a{color:var(--white);font-size:11.5px;line-height:1;text-decoration:none;text-transform:uppercase;white-space:nowrap}
.brand{position:absolute;left:88px;top:62px;display:flex;align-items:center;gap:14px;z-index:3}
.brand-mark{width:62px;height:62px;border-radius:50%;background:var(--navy)}
.brand-name{color:var(--navy);font-size:19px;font-weight:700;line-height:1.2;text-transform:uppercase}
.hero{position:absolute;left:88px;top:84px;width:825px;height:502px;border:3px solid var(--white);
  background:linear-gradient(100deg,#4b4844 0%,#7a6a5a 25%,#b9aa98 48%,#6d4a38 62%,#3f3b52 80%,#7d8190 100%);z-index:1}
.hero-dots{position:absolute;left:146px;bottom:4px;display:flex;gap:3px}
.hero-dots span{width:15px;height:15px;border-radius:50%;background:#cfcfcf;border:1px solid #999}
.hero-dots span.is-active{background:var(--orange);border-color:var(--orange-dark)}
.welcome{position:absolute;left:510px;top:382px;width:383px;height:188px;background:var(--navy);border:4px solid #b8b8b8;padding:10px 16px;color:var(--white);z-index:3}
.welcome h1{font-size:15px;font-weight:400;line-height:1.15;margin-bottom:9px}
.welcome h1 strong{font-weight:700}
.welcome p{font-family:Arial,sans-serif;font-size:11px;line-height:17px}
.section-menu{position:absolute;left:735px;top:30px;width:196px;height:205px;background:var(--orange);border-radius:0 0 6px 6px;padding:10px 16px 0 16px;z-index:3;box-shadow:0 6px 0 -1px #0d1634}
.section-menu a{display:block;color:var(--white);font-size:13.5px;text-transform:uppercase;text-decoration:none;line-height:25px;white-space:nowrap;border-bottom:1px dotted rgba(255,255,255,.6);padding-left:10px;position:relative}
.section-menu a:last-child{border-bottom:none}
.section-menu a::before{content:"";position:absolute;left:0;top:10px;border-left:4px solid var(--white);border-top:3px solid transparent;border-bottom:3px solid transparent}
.strapline{position:absolute;left:87px;top:590px;color:var(--white);font-size:16.5px;font-weight:700}
.content-band{position:absolute;left:0;top:622px;width:1000px;height:318px;background:var(--navy-deep)}
.cards{position:absolute;left:87px;top:17px;width:826px;height:273px;display:flex;gap:5px;border-radius:4px;overflow:hidden}
.card{flex:1;padding:12px 12px 0;position:relative}
.card--news{background:var(--card-news)}
.card--projects{background:var(--card-projects)}
.card--district{background:var(--card-district)}
.card h2{font-size:19px;font-weight:400;color:var(--ink);padding-bottom:6px;border-bottom:3px solid var(--orange);margin-bottom:17px}
.card p{font-family:Arial,sans-serif;font-size:10.8px;line-height:17px;color:var(--body-text);letter-spacing:-.1px}
.news-item{border-bottom:1px dotted #b9b4aa;padding-bottom:5px;margin-bottom:7px}
.news-item:last-of-type{border-bottom:none}
.more{position:absolute;right:18px;bottom:15px;background:var(--orange);color:var(--white);font-size:11px;font-weight:700;padding:1px 6px 2px 6px;text-decoration:none}
.more::after{content:"";position:absolute;right:0;bottom:-6px;border-left:6px solid transparent;border-top:6px solid var(--orange-dark)}
.site-footer{position:absolute;left:0;top:940px;width:1000px;height:110px;background:var(--navy-foot);border-top:2px dashed #33447c}
.footer-col{position:absolute;top:12px}
.footer-col h3{color:var(--orange);font-size:15px;font-weight:400;margin-bottom:9px}
.footer-col ul{list-style:none;font-family:Arial,sans-serif;font-size:11px;line-height:17px;color:var(--white);white-space:nowrap}
.footer-links{left:87px}
.footer-links .cols{display:flex;gap:50px}
.footer-location{left:389px}
.footer-location .cols{display:flex;gap:27px}
.footer-social{left:728px}
.social-icons{display:flex;gap:11px;margin-bottom:6px}
.social-icons span{width:26px;height:26px;border-radius:3px;background:#5677b5}
.social-icons span:nth-child(4){background:var(--orange)}
.footer-email{font-family:Arial,sans-serif;font-size:11px;color:var(--white)}
</style>
</head>
<body>
<div class="page">
  <div class="hero" role="img" aria-label="Photo of a smiling schoolgirl in a classroom beside a drawn tree of letters and numbers">
    <div class="hero-dots"><span class="is-active"></span><span></span><span></span><span></span><span></span></div>
  </div>

  <svg class="header-wave" width="1000" height="180" viewBox="0 0 1000 180" aria-hidden="true">
    <path d="M0,0 H1000 V32 C900,18 800,22 700,60 C500,138 220,160 0,138 Z" fill="#ffffff"/>
    <path d="M0,138 C220,160 500,138 700,60 C800,22 900,18 1000,32" fill="none" stroke="#f5a313" stroke-width="9"/>
    <path d="M0,147 C220,170 500,147 700,69" fill="none" stroke="#e08e00" stroke-width="4" opacity=".6"/>
  </svg>

  <nav class="main-nav">
    <a href="#">Home</a><a href="#">About the VJRCD</a><a href="#">Management Teams</a><a href="#">Contact the VJRCD</a>
  </nav>

  <div class="brand">
    <span class="brand-mark"></span>
    <span class="brand-name">Velmora<br>Schooling Bureau</span>
  </div>

  <nav class="section-menu">
    <a href="#">Project</a><a href="#">Latest News</a><a href="#">Structure</a><a href="#">Goals</a><a href="#">Consultants</a><a href="#">Service Providers</a><a href="#">District Involment</a>
  </nav>

  <section class="welcome">
    <h1>Welcome to &nbsp;<strong>Velmora Junior Reading &amp; Counting Drive</strong></h1>
    <p>Lorem ipsum dolor sit amet, consectetur adipisicing elit, sed do eiusmod tempor incididunt ut labore et dolore magna aliqua. Ut enim ad minim veniam, quis nostrud exercitation ullamco laboris nisi ut aliquip ex ea commodo consequat. Duis aute irure dolor in reprehenderit in voluptate velit esse cillum dolore eu fugiat nulla pariatur. Excepteur sint occaecat cupidatat non proident, sunt in culpa</p>
  </section>

  <div class="strapline">Velmora Junior Reading &amp; Counting Drive</div>

  <main class="content-band">
    <div class="cards">
      <article class="card card--news">
        <h2>Latest News</h2>
        <p class="news-item">Lorem ipsum dolor sit amet, consectetur adipiscing elit. Nam vel metus eget massa varius vehicula.</p>
        <p class="news-item">Vivamus accumsan lorem eget nisl placerat vel condimentum quam ultrices.</p>
        <p class="news-item">Lorem ipsum dolor sit amet, consectetur adipiscing elit. Nam vel metus eget massa varius vehicula.</p>
        <p class="news-item">Vivamus accumsan lorem eget nisl placerat vel condimentum quam ultrices.</p>
        <a class="more" href="#">More</a>
      </article>
      <article class="card card--projects">
        <h2>Projects</h2>
        <p>Lorem ipsum dolor sit amet, consectetur adipisicing elit, sed do eiusmod tempor incididunt ut labore et dolore magna aliqua. Ut enim ad minim veniam, quis nostrud exercitation ullamco laboris nisi ut aliquip ex ea commodo consequat. Duis aute irure dolor in reprehenderit in voluptate velit esse cillum dolore eu fugiat nulla pariatur. Excepteur sint occaecat cupidatat non proident, sunt in culpa qui officia deserunt mollit anim id est laborum</p>
        <a class="more" href="#">More</a>
      </article>
      <article class="card card--district">
        <h2>District Involvements</h2>
        <p>Lorem ipsum dolor sit amet, consectetur adipisicing elit, sed do eiusmod tempor incididunt ut labore et dolore magna aliqua. Ut enim ad minim veniam, quis nostrud exercitation ullamco laboris nisi ut aliquip ex ea commodo consequat. Duis aute irure dolor in reprehenderit in voluptate velit esse cillum dolore eu fugiat nulla pariatur. Excepteur sint occaecat cupidatat non proident, sunt in culpa qui officia deserunt mollit anim id est laborum</p>
        <a class="more" href="#">More</a>
      </article>
    </div>
  </main>

  <footer class="site-footer">
    <div class="footer-col footer-links">
      <h3>Quick Links</h3>
      <div class="cols">
        <ul><li>Home</li><li>About the VJRCD</li><li>Management Team</li></ul>
        <ul><li>Latest News</li><li>Support</li><li>Contact The VJRCD</li></ul>
      </div>
    </div>
    <div class="footer-col footer-location">
      <h3>Our Location</h3>
      <div class="cols">
        <ul><li>Miriam Okafor</li><li>42 Larkspur Avenue</li><li>Velmora City, 4100</li></ul>
        <ul><li>Phone: 021 555 0140</li><li>Fax: 021 555 0141</li><li>Cell: 071 555 0192</li></ul>
      </div>
    </div>
    <div class="footer-col footer-social">
      <h3>Social Network</h3>
      <div class="social-icons" aria-label="Social network links"><span></span><span></span><span></span><span></span></div>
      <p class="footer-email">Email:info@vjrcd.example</p>
    </div>
  </footer>
</div>
</body>
</html>
```